Velmora - New coded website

Current website is around 5 years old and corrupted in some ways...
I would like to refresh the design and to create a new coded website based on the current content .
Please refer to :
www.velmora-sample.com.au

Coded - Design and coding required

```html
<!DOCTYPE html>
<html lang="en">
<head>
<meta charset="utf-8">
<title>Velmora – Odours Controlled Naturally</title>
<link href="https://fonts.googleapis.com/css2?family=Poppins:ital,wght@0,400;0,500;0,600;1,400&display=swap" rel="stylesheet">
<style>
:root{
  --navy:#0a1c28;
  --navy-2:#0d3550;
  --green:#6cc04a;
  --green-dark:#4fa334;
  --teal:#1e8a73;
  --white:#ffffff;
  --text-dark:#2b3a44;
  --muted:#7d8a92;
  --card-bg:#eef2f6;
}
*{box-sizing:border-box;margin:0;padding:0}
html,body{width:1200px;height:4709px;overflow:hidden}
body{font-family:'Poppins',sans-serif;background:var(--navy);color:var(--white);position:relative}
.sec{position:absolute;left:0;width:1200px}
.h2{font-weight:500;text-transform:uppercase;text-align:center;font-size:34px;letter-spacing:.5px}
.btn{display:inline-flex;align-items:center;gap:18px;background:var(--green);color:#fff;border-radius:30px;font-size:12px;font-weight:600;text-transform:uppercase;padding:0 6px 0 24px;height:42px}
.btn .arrow{width:32px;height:32px;border-radius:50%;background:#fff;display:flex;align-items:center;justify-content:center}

/* header */
.topbar{top:0;height:95px;background:var(--navy)}
.brand{position:absolute;left:80px;top:22px;display:flex;align-items:center;gap:10px;font-size:30px;font-weight:500;color:#fff}
.brand .dot{width:48px;height:48px;border-radius:50%;background:var(--green)}
.topbar .btn{position:absolute;left:449px;top:26px;height:42px;background:var(--teal)}
.socials{position:absolute;left:680px;top:38px;display:flex;gap:30px}
.socials span{width:16px;height:16px;border-radius:3px;background:#fff;display:block}
.phone-band{position:absolute;right:0;top:0;width:340px;height:95px;background:var(--green);clip-path:polygon(15% 0,100% 0,100% 100%,0 100%)}
.phone{position:absolute;right:38px;top:28px;display:flex;align-items:center;gap:18px;font-size:21px;font-weight:500}
.phone .ic{width:40px;height:40px;border-radius:50%;background:var(--navy-2);display:flex;align-items:center;justify-content:center}
.nav{top:95px;height:50px;background:var(--navy-2);display:flex;gap:27px;padding-left:139px;align-items:center;font-size:12px;font-weight:600;text-transform:uppercase}

/* hero */
.hero{top:145px;height:600px;background:linear-gradient(180deg,#d9e6e8 0%,#b9ccc4 35%,#8fa95a 62%,#567f25 100%)}
.hero h1{position:absolute;left:143px;top:160px;font-size:56px;line-height:66px;font-weight:500;color:var(--navy)}
.hero .btn{position:absolute;left:143px;top:387px}

/* products */
.products{top:745px;height:656px}
.products .h2{margin-top:110px}
.prod-row{position:absolute;top:213px;left:143px;width:914px;display:flex;justify-content:space-between}
.prod{width:240px;text-align:center}
.prod .ring{width:240px;height:240px;border-radius:50%;border:10px solid var(--teal);border-bottom-color:transparent;padding:6px}
.prod .ring.g{border-color:var(--green);border-bottom-color:transparent}
.prod .photo{width:100%;height:100%;border-radius:50%}
.prod .mark{width:36px;height:36px;border-radius:50%;background:var(--green);margin:-12px auto 18px}
.prod h3{font-size:19px;font-weight:600;line-height:26px;text-transform:uppercase}

/* about */
.about{top:1401px;height:578px;background:linear-gradient(180deg,#1f3a48,#2c4a42)}
.about .photo{position:absolute;left:80px;top:86px;width:471px;height:406px;border-radius:12px;background:linear-gradient(180deg,#e6ecd9 0%,#8fb05d 45%,#4f7f22 100%)}
.about .copy{position:absolute;left:613px;top:82px;width:510px}
.about h2{font-size:32px;font-weight:500;line-height:42px;text-transform:uppercase}
.about p{margin-top:22px;font-size:14.5px;line-height:26.5px}
.about p em{color:var(--green);font-style:normal}
.about .btn{margin-top:24px}

/* testimonials */
.reviews{top:1979px;height:615px}
.reviews .h2{margin-top:98px;line-height:46px}
.rev-row{position:absolute;top:229px;left:145px;width:912px;display:flex;justify-content:space-between}
.rev{width:287px}
.rev .bubble{background:#fff;border-radius:4px;padding:22px 24px;height:206px;color:var(--muted);font-size:13px;line-height:23.5px;text-align:justify;position:relative}
.rev .bubble::after{content:"";position:absolute;left:40px;bottom:-14px;border:14px solid transparent;border-bottom:0;border-top-color:#fff}
.stars{color:var(--teal);letter-spacing:3px;font-size:14px;margin-bottom:6px}
.who{display:flex;gap:20px;margin-top:20px;align-items:center}
.who .av{width:70px;height:70px;border-radius:50%;border:4px solid var(--green);background:#9aa7ae;flex:none}
.who b{display:block;font-size:14px;font-weight:600;text-transform:uppercase}
.who small{font-size:11px;line-height:17px;display:block;margin-top:6px}

/* best */
.best{top:2594px;height:446px;background:linear-gradient(180deg,#79c454,#4f9d35)}
.best .h2{margin-top:62px}
.best-row{position:absolute;top:153px;left:80px;width:1040px;display:flex;justify-content:space-between}
.feat{width:232px;height:220px;background:#fff;color:var(--navy);text-align:center;padding-top:36px}
.feat .ic{width:86px;height:86px;border-radius:50%;background:var(--teal);margin:0 auto 28px;display:flex;align-items:center;justify-content:center}
.feat h4{font-size:13px;font-weight:600;text-transform:uppercase;line-height:22px;padding:0 18px}

/* projects */
.projects{top:3040px;height:880px}
.projects .h2{margin-top:118px}
.big{position:absolute;left:145px;top:201px;width:446px;height:558px;background:var(--card-bg);color:var(--navy)}
.big .photo{height:384px;background:linear-gradient(180deg,#a7a69c,#565c58)}
.big .txt{padding:42px 40px;font-style:italic;font-size:16px;line-height:24px}
.more{display:inline-block;color:var(--green);font-style:normal;font-weight:600;font-size:13px;text-decoration:underline;margin-top:18px}
.small{position:absolute;left:607px;width:448px;height:174px;background:var(--card-bg);color:var(--navy);display:flex}
.small .photo{width:200px;flex:none;background:linear-gradient(180deg,#b8c8cc,#4f6a4f)}
.small .txt{padding:18px 22px 0 30px;font-style:italic;font-size:14.5px;line-height:22.5px}
.small .more{margin-top:4px}

/* contact */
.contact{top:3920px;height:459px;background:linear-gradient(180deg,#1e8a73,#1a5a5a)}
.contact .h2{margin-top:66px}
.field{position:absolute;background:#fff;color:var(--muted);font-size:12px;padding:14px 18px}
.submit{position:absolute;left:517px;top:337px;width:168px;height:46px;border-radius:24px;background:var(--green);font-size:14px;font-weight:600;text-align:center;line-height:46px}

/* footer */
.footer{top:4379px;height:330px}
.footer .brand{left:145px;top:137px}
.fcol{position:absolute;top:64px}
.fcol h5{font-size:16px;font-weight:600;text-transform:uppercase;padding-bottom:10px;border-bottom:2px solid var(--green);display:inline-block;margin-bottom:16px}
.fcol li{list-style:none;font-size:11px;line-height:27px;padding-left:6px}
.cline{display:flex;gap:14px;font-size:11px;line-height:18px;margin-bottom:14px}
.cline .ic{width:22px;height:22px;border-radius:50%;background:var(--green);flex:none}
.sub p{font-size:11px;line-height:19px;width:240px}
.sub .box{margin-top:14px;width:240px;height:34px;background:#fff;border-radius:4px;display:flex;justify-content:space-between;color:var(--muted);font-size:10px;align-items:center;padding-left:12px;overflow:hidden}
.sub .box span{width:46px;height:34px;background:var(--green);display:flex;align-items:center;justify-content:center}
.copy-line{position:absolute;left:143px;top:296px;font-size:12px}
.copy-line u{color:var(--green)}
.fsoc{position:absolute;left:924px;top:294px;display:flex;gap:8px}
.fsoc span{width:28px;height:28px;border-radius:50%;background:#fff;display:block}
.fsoc span:nth-child(2){background:var(--green)}
</style>
</head>
<body>

<header class="sec topbar">
  <div class="brand"><span class="dot"></span>Velmora</div>
  <div class="btn">Request a quote <span class="arrow"><svg width="12" height="12" viewBox="0 0 12 12"><path d="M4 2l4 4-4 4" stroke="#1e8a73" stroke-width="2" fill="none"/></svg></span></div>
  <div class="socials"><span></span><span></span><span></span><span></span></div>
  <div class="phone-band"></div>
  <div class="phone"><span class="ic"><svg width="18" height="18" viewBox="0 0 24 24"><path fill="#fff" d="M6.6 10.8a15 15 0 006.6 6.6l2.2-2.2c.3-.3.7-.4 1-.2 1.1.4 2.3.6 3.6.6.6 0 1 .4 1 1V20c0 .6-.4 1-1 1A17 17 0 013 4c0-.6.4-1 1-1h3.5c.6 0 1 .4 1 1 0 1.3.2 2.5.6 3.6.1.3 0 .7-.2 1z"/></svg></span>100 - 555 - 0199</div>
</header>
<nav class="sec nav"><span>Odour control products</span><span>How biofiltration works</span><span>Odour control by industry</span><span>Past projects</span><span>About us</span><span>Contact</span></nav>

<section class="sec hero" role="img" aria-label="Woman with raised arms standing in a sunlit grass meadow with hills">
  <h1>ODOURS<br>CONTROLLED<br>NATURALLY</h1>
  <div class="btn">Request a quote <span class="arrow"><svg width="12" height="12" viewBox="0 0 12 12"><path d="M4 2l4 4-4 4" stroke="#6cc04a" stroke-width="2" fill="none"/></svg></span></div>
</section>

<section class="sec products">
  <h2 class="h2">Odour control products</h2>
  <div class="prod-row">
    <div class="prod"><div class="ring"><div class="photo" role="img" aria-label="Above ground biofilter tank installation" style="background:linear-gradient(160deg,#b9b4a6,#6f746c)"></div></div><div class="mark"></div><h3>Above ground:<br>VelVent S1</h3></div>
    <div class="prod"><div class="ring g"><div class="photo" role="img" aria-label="Below ground biofilter under a driveway" style="background:linear-gradient(160deg,#c9d3c2,#75895a)"></div></div><div class="mark"></div><h3>Below ground:<br>VelVent M2</h3></div>
    <div class="prod"><div class="ring"><div class="photo" role="img" aria-label="Final treatment carbon filter tanks" style="background:linear-gradient(160deg,#d7dde0,#8c9a88)"></div></div><div class="mark"></div><h3>Final treatment:<br>VelCarb</h3></div>
  </div>
</section>

<section class="sec about">
  <div class="photo" role="img" aria-label="Woman relaxing on a green hillside meadow"></div>
  <div class="copy">
    <h2>Odour control solutions about Velmora</h2>
    <p>Velmora uses sustainable biotechnology to resolve odour and <em>corrosion</em> problems in a highly efficient, environmentally friendly and cost-effective manner. Our, products, the VelVent series of biofilters have been specifically engineered to overcome issues traditionally associated with biofiltration, such as bed compaction and uneven moisture levels, and our patented design achieves a removal rate of up to 99.9% per stage of treatment.</p>
    <div class="btn">Request a quote <span class="arrow"><svg width="12" height="12" viewBox="0 0 12 12"><path d="M4 2l4 4-4 4" stroke="#6cc04a" stroke-width="2" fill="none"/></svg></span></div>
  </div>
</section>

<section class="sec reviews">
  <h2 class="h2">As soon as the system was started,<br>the smell disappeared!</h2>
  <div class="rev-row">
    <div class="rev"><div class="bubble"><div class="stars">★★★★★</div>Marco and the Velmora team promised to stop the odour from our smelly neighbor and they delivered- in spades! As soon as the system was started, the smell disappeared.</div><div class="who"><div class="av" role="img" aria-label="Customer portrait"></div><div><b>Rhys Calder</b><small>Nearby resident to Elm Row<br>Wastewater Pump Station</small></div></div></div>
    <div class="rev"><div class="bubble"><div class="stars">★★★★★</div>Marco and the Velmora team promised to stop the odour from our smelly neighbor and they delivered- in spades! As soon as the system was started, the smell disappeared.</div><div class="who"><div class="av" role="img" aria-label="Customer portrait"></div><div><b>Rhys Calder</b><small>Nearby resident to Elm Row<br>Wastewater Pump Station</small></div></div></div>
    <div class="rev"><div class="bubble"><div class="stars">★★★★★</div>Marco and the Velmora team promised to stop the odour from our smelly neighbor and they delivered- in spades! As soon as the system was started, the smell disappeared.</div><div class="who"><div class="av" role="img" aria-label="Customer portrait"></div><div><b>Rhys Calder</b><small>Nearby resident to Elm Row<br>Wastewater Pump Station</small></div></div></div>
  </div>
</section>

<section class="sec best">
  <h2 class="h2">What makes us the best?</h2>
  <div class="best-row">
    <div class="feat"><div class="ic"><svg width="40" height="40" viewBox="0 0 40 40" fill="none" stroke="#fff" stroke-width="2.5"><circle cx="20" cy="20" r="8"/><path d="M20 4v6M20 30v6M4 20h6M30 20h6"/></svg></div><h4>Biological &amp; sustainable technology</h4></div>
    <div class="feat"><div class="ic"><svg width="40" height="40" viewBox="0 0 40 40" fill="none" stroke="#fff" stroke-width="2.5"><circle cx="20" cy="20" r="12"/><path d="M16 14h6a3 3 0 010 6h-6v8"/></svg></div><h4>Efficient maintenance cost</h4></div>
    <div class="feat"><div class="ic"><svg width="40" height="40" viewBox="0 0 40 40" fill="none" stroke="#fff" stroke-width="2.5"><path d="M6 20l8-8 10 2 10 6-4 10-14 2-8-6z"/></svg></div><h4>100% Australian owned</h4></div>
    <div class="feat"><div class="ic"><svg width="40" height="40" viewBox="0 0 40 40" fill="none" stroke="#fff" stroke-width="2.5"><path d="M6 30h8l10 2 10-6M20 22V10M20 14c-4 0-6-3-6-6 4 0 6 3 6 6zM20 14c4 0 6-3 6-6-4 0-6 3-6 6z"/></svg></div><h4>Eco friendly</h4></div>
  </div>
</section>

<section class="sec projects">
  <h2 class="h2">Past projects</h2>
  <div class="big"><div class="photo" role="img" aria-label="Aerial view of biofilter tanks at a treatment plant"></div><div class="txt">6750 m3/h- H2S 35ppm- Harlow Bay Wastewater Treatment Plant<br><span class="more">Read More</span></div></div>
  <div class="small" style="top:201px"><div class="photo" role="img" aria-label="Green biofilter tanks at a pump station"></div><div class="txt">3000 m3/h- H2S 250ppm - Elm Row Pump Station: preventing odours and corrosion in water infrastructure<br><span class="more">Read More</span></div></div>
  <div class="small" style="top:393px"><div class="photo" role="img" aria-label="Biofilter tanks beside a building"></div><div class="txt">3000 m3/h- H2S 400ppm- Kestrel Park SPS: Odour treatment for balance tanks &amp; wastewater infrastructure<br><span class="more">Read More</span></div></div>
  <div class="small" style="top:585px"><div class="photo" role="img" aria-label="Odour control tanks at a reclamation plant"></div><div class="txt">2800 m3/h- H2S 300ppm- Tallowin Shire Council Wastewater Reclamation Plant Odour Control System<br><span class="more">Read More</span></div></div>
</section>

<section class="sec contact">
  <h2 class="h2">Contact us</h2>
  <div class="field" style="left:227px;top:144px;width:364px;height:44px">Your Name</div>
  <div class="field" style="left:227px;top:205px;width:364px;height:44px">Email Address</div>
  <div class="field" style="left:227px;top:266px;width:364px;height:44px">Phone Number</div>
  <div class="field" style="left:605px;top:144px;width:368px;height:167px">Feedback</div>
  <div class="submit">SUBMIT NOW</div>
</section>

<footer class="sec footer">
  <div class="brand"><span class="dot"></span>Velmora</div>
  <div class="fcol" style="left:357px"><h5>Quick links</h5><ul><li>Odour Control Products</li><li>How Biofiltration Works</li><li>Odour Control by Industry</li><li>Past Projects</li><li>About Us</li></ul></div>
  <div class="fcol" style="left:565px"><h5>Contact us</h5><div class="cline"><span class="ic"></span>+61 (08) 5550 0142</div><div class="cline"><span class="ic"></span>12 Sample Lane,<br>Greenvale WA 6000, Australia</div></div>
  <div class="fcol sub" style="left:816px"><h5>Subscribe</h5><p>Sign up today to get resources on how to attract and retain more customers!</p><div class="box">Email Address<span><svg width="14" height="14" viewBox="0 0 14 14"><path d="M1 7l12-6-4 12-2-5z" fill="#fff"/></svg></span></div></div>
  <div class="copy-line">Copyright© 2023 <u>Velmora</u> | All Rights Reserved</div>
  <div class="fsoc"><span></span><span></span><span></span><span></span></div>
</footer>

</body>
</html>
```